IT Management and Consulting company wants a design

The website should transfer an innovative, forward-oriented, optimistic, and serious image to my customer. Because we work in an agile, the design should transfer this approach.

The new color should make a serious, but not boring, impression for the business visitors of top-level companies.

The main focus topics are:
* IT strategy consulting
* Digital transformation
* IT quality management

The website should be in the English language.

The website should be created for WordPress. The existing website is http://www.t-vork.com (no WordPress) is provided by servalpin.de. A WordPress sandbox system exists.

Target Market(s)

Purchasing departments, IT decision makers from companies, project recruiting companies

Industry/Entity Type

IT-Provider, Telecommunication, Automotive

Coding

Coded - Design and coding required

Number of Pages Required

4 page

Font styles to use
Serif
Sans Serif

Requirements
Must have
• Long-pager scrolling, a detail page for each portfolio topics, contact page, page about the company
Nice to have
• Parallax animation less is more, maybe a nice Hero Video Header, interessting 3D graph, Isometric graphs will bi nice, more clean than overloaded,
Should not have
• personal recruting page like in www.t-vork.com

```html
<!DOCTYPE html>
<html lang="en">
<head>
<meta charset="utf-8">
<title>Tervork Consulting – IT Management &amp; Consulting</title>
<link href="https://fonts.googleapis.com/css2?family=Exo+2:wght@400;500;600;700&family=Open+Sans:ital,wght@0,400;0,600;0,700;1,400&family=Rubik:wght@500;700&display=swap" rel="stylesheet">
<style>
:root{
  --teal:#2aa9a9;
  --teal-dark:#1d8e90;
  --teal-light:#3fc1bf;
  --navy:#0b1a29;
  --navy-mid:#13283c;
  --heading:#174463;
  --text:#5d6670;
  --muted:#8a939b;
  --white:#ffffff;
  --orange:#e05a2c;
  --blue:#2459c8;
}
*{box-sizing:border-box;margin:0;padding:0}
html,body{width:1200px;height:5008px;overflow:hidden}
body{font-family:"Open Sans",sans-serif;color:var(--text);background:var(--white);position:relative}
section,header,footer{position:absolute;left:0;width:1200px;overflow:hidden}
.abs{position:absolute}
.heading-font{font-family:"Exo 2",sans-serif}

/* hero */
.hero{top:0;height:714px;background:radial-gradient(ellipse at 62% 45%,#1d4a5e 0%,#0f2a3a 40%,#08141f 100%)}
.hero-visual{position:absolute;inset:0}
.brand{left:58px;top:30px;color:var(--white)}
.brand-name{font-family:"Exo 2",sans-serif;font-size:22px;font-weight:500;display:flex;align-items:center;gap:8px}
.brand-dot{width:8px;height:8px;border-radius:50%;background:var(--teal-light)}
.brand-tag{font-size:9px;color:#9fb3bf;margin-left:16px;letter-spacing:.5px}
.nav{right:310px;top:31px;display:flex;gap:22px;font-size:12px;color:var(--white)}
.nav .active{color:var(--teal-light)}
.hero-phone{left:918px;top:20px;display:flex;align-items:center;gap:10px;color:var(--white);font-size:15px}
.icon-circle{width:36px;height:36px;border-radius:50%;background:var(--teal);display:flex;align-items:center;justify-content:center}
.hero-title{left:58px;top:302px;font-family:"Rubik",sans-serif;font-weight:500;font-size:46px;line-height:53px;color:var(--white)}
.hero-title span{color:var(--teal-light)}
.hero-sub{left:60px;top:474px;font-size:16px;color:var(--teal-light)}
.play{left:812px;top:374px;width:92px;height:92px;border-radius:50%;background:var(--teal);display:flex;align-items:center;justify-content:center}
.play-inner{width:66px;height:66px;border-radius:50%;border:5px solid var(--white);display:flex;align-items:center;justify-content:center}
.watch{left:949px;top:406px;font-size:18px;color:var(--white)}

/* band */
.band{top:714px;height:74px;background:linear-gradient(#fff,#f2f4f5);box-shadow:0 6px 10px rgba(0,0,0,.08);z-index:2;text-align:center;line-height:74px;font-family:"Exo 2",sans-serif;font-weight:600;font-size:22px;color:var(--heading)}

/* about */
.about{top:788px;height:570px;text-align:center}
.section-title{font-family:"Exo 2",sans-serif;font-size:36px;color:var(--heading);font-weight:400}
.section-title b{font-weight:700}
.about .section-title{position:absolute;top:72px;width:100%}
.about .sub{position:absolute;top:124px;width:100%;font-size:14px;color:#444}
.about p{position:absolute;left:360px;width:480px;font-size:12px;line-height:20px;color:var(--muted)}
.about .quote{font-style:italic;color:var(--teal-dark);font-size:14px;line-height:22px;left:340px;width:520px}
.feature{position:absolute;top:370px;width:140px;text-align:center}
.feature-circle{width:96px;height:96px;border-radius:50%;background:var(--teal);margin:0 auto;display:flex;align-items:center;justify-content:center;box-shadow:0 0 0 5px #e4f4f4}
.feature-label{margin-top:18px;font-family:"Exo 2",sans-serif;font-weight:600;font-size:16px;color:#333;letter-spacing:1px}
.feature-line{position:absolute;top:418px;height:0;border-top:2px dotted #9fd3d3}

/* dark topics */
.topic-dark{background:linear-gradient(90deg,#0a1826 0%,#102a40 55%,#0b1a29 100%);color:var(--white)}
.strategy{top:1358px;height:451px}
.quality{top:2260px;height:449px;background:linear-gradient(180deg,#0c1b2a 0%,#13293d 60%,#1b2c3a 100%)}
.topic-title{font-family:"Exo 2",sans-serif;font-size:30px;font-weight:500;color:var(--white)}
.topic-text{font-size:12.5px;line-height:21px;color:#d2dbe2;width:375px}
.digital{top:1809px;height:451px;background:radial-gradient(ellipse at 35% 45%,#3cbcbc 0%,var(--teal) 55%,#259a9b 100%);color:var(--white)}
.chart-label{font-size:11px;fill:#e4ecf0;font-family:"Open Sans",sans-serif}

/* portfolio */
.portfolio{top:2709px;height:1016px;text-align:center}
.portfolio .section-title{position:absolute;top:70px;width:100%}
.portfolio .sub{position:absolute;top:124px;width:100%;font-size:14px;color:#333}
.portfolio .intro{position:absolute;top:164px;left:300px;width:600px;font-size:12px;line-height:22px;color:var(--muted)}
.card{position:absolute;width:420px;text-align:left}
.card-media{width:420px;height:263px}
.card-title{font-family:"Exo 2",sans-serif;font-weight:600;font-size:20px;color:var(--heading);margin-top:24px}
.card-desc{font-size:12px;color:var(--muted);margin-top:4px;padding-left:2px}

/* contact */
.contact{top:3725px;height:498px;background:linear-gradient(180deg,#2aa9a9,#239596);text-align:center;color:var(--white)}
.contact-bg{position:absolute;inset:0;background:radial-gradient(ellipse at 85% 30%,rgba(255,255,255,.12),transparent 60%)}
.contact .section-title{position:absolute;top:80px;width:100%;color:var(--white)}
.contact .sub{position:absolute;top:124px;width:100%;font-size:13px}
.field{position:absolute;height:40px;background:var(--white);border-radius:3px;color:#8a8a8a;font-size:11px;text-align:left;padding:12px 14px}
.submit{position:absolute;left:539px;top:383px;width:120px;height:38px;border:2px solid var(--white);border-radius:8px;font-family:"Exo 2",sans-serif;font-weight:600;font-size:15px;line-height:34px;letter-spacing:1px}

/* experience */
.experience{top:4223px;height:449px;background:#f0f1f2}
.exp-media{position:absolute;left:0;top:0;width:603px;height:449px}
.exp-lead{left:648px;top:78px;font-family:"Exo 2",sans-serif;font-size:26px;font-weight:600;color:var(--heading)}
.exp-title{left:648px;top:118px;font-family:"Exo 2",sans-serif;font-size:42px;font-weight:500;color:var(--teal)}
.exp-text{left:648px;top:174px;font-size:21px;line-height:32px;color:#2c3e50;width:420px}
.exp-phone{left:645px;top:268px;display:flex;align-items:center;gap:20px}
.exp-phone .ring{width:72px;height:72px;border-radius:50%;border:2px solid var(--teal);display:flex;align-items:center;justify-content:center}
.exp-phone .icon-circle{width:60px;height:60px}
.exp-phone small{display:block;font-size:14px;color:#333}
.exp-phone strong{display:block;font-size:24px;color:var(--heading);margin-top:4px}

/* footer */
.footer{top:4672px;height:336px;background:var(--navy);color:#c8d2da}
.footer .brand{top:60px}
.footer-text{left:58px;top:128px;width:420px;font-size:12px;line-height:22px}
.footer-text a{color:var(--teal-light);text-decoration:none}
.footer-heading{font-family:"Exo 2",sans-serif;font-weight:600;font-size:16px;color:var(--teal-light);letter-spacing:1px}
.sitemap{left:568px;top:50px}
.sitemap ul{list-style:none;margin-top:18px}
.sitemap li{font-size:12px;height:26.5px;padding-left:18px;position:relative}
.sitemap li::before{content:"";position:absolute;left:0;top:6px;width:5px;height:5px;border-radius:50%;background:var(--teal-light)}
.contact-info{left:844px;top:50px}
.info-row{position:absolute;left:0;display:flex;gap:20px;font-size:12px;line-height:19px;width:320px}
.info-icon{width:30px;height:30px;background:var(--teal);border-radius:4px;display:flex;align-items:center;justify-content:center;flex:none}
.copyright{left:0;top:268px;width:1200px;border-top:1px solid #1e3347;text-align:center;padding-top:20px;font-size:12px}
.copyright span{color:var(--teal-light)}
</style>
</head>
<body>

<header class="hero">
  <div class="hero-visual" role="img" aria-label="Wireframe rendering of a car with digital measurement overlays on a dark blue background"></div>
  <div class="abs brand">
    <div class="brand-name"><span class="brand-dot"></span>Tervork Consulting</div>
    <div class="brand-tag">power of competence</div>
  </div>
  <nav class="abs nav">
    <span class="active">Home</span><span>Companies</span><span>Portfolio</span><span>Scouting</span><span>Contact Us</span>
  </nav>
  <div class="abs hero-phone">
    <div class="icon-circle"><svg width="18" height="18" viewBox="0 0 24 24"><path fill="#fff" d="M6.6 10.8a15.1 15.1 0 0 0 6.6 6.6l2.2-2.2c.3-.3.7-.4 1-.2 1.1.4 2.3.6 3.6.6.6 0 1 .4 1 1V20c0 .6-.4 1-1 1A17 17 0 0 1 3 4c0-.6.4-1 1-1h3.5c.6 0 1 .4 1 1 0 1.3.2 2.5.6 3.6.1.3 0 .7-.2 1z"/></svg></div>
    <span>+49 (0) 5521 7704410</span>
  </div>
  <h1 class="abs hero-title">In <span>Compliance</span> With<br>All Time And Cost<br>Specifications.</h1>
  <p class="abs hero-sub">Automotive and Telecommunications Consulting Services.</p>
  <div class="abs play"><div class="play-inner"><svg width="26" height="30" viewBox="0 0 26 30"><path fill="#fff" d="M4 2l20 13L4 28z"/></svg></div></div>
  <div class="abs watch">Watch Video</div>
</header>

<div class="band" style="position:absolute;left:0;width:1200px">Professional Method For Project Success</div>

<section class="about">
  <h2 class="section-title"><b>Tervork</b> Consulting</h2>
  <div class="sub">Power of Cometence</div>
  <p style="top:167px">Tervork Consulting GmbH was founded by Lukas Tervo in 2010 and has been operating successfully on the market ever since.</p>
  <p class="quote" style="top:216px">Use guarantee of success: Concentration on the essentials, customer orientation and experience</p>
  <p style="top:270px">Thanks to more than 25 years of activity in project management and consulting, mainly for medium-sized and large companies, Tervork Consulting is very familiar with the challenges in all project phases of complex IT projects.</p>
  <div class="feature-line" style="left:370px;width:170px"></div>
  <div class="feature-line" style="left:658px;width:170px"></div>
  <div class="feature" style="left:241px">
    <div class="feature-circle"><svg width="50" height="50" viewBox="0 0 50 50" fill="none" stroke="#fff" stroke-width="2"><path d="M25 40s-11-12-11-20a11 11 0 0 1 22 0c0 8-11 20-11 20z"/><circle cx="25" cy="20" r="4"/><ellipse cx="25" cy="42" rx="12" ry="3"/></svg></div>
    <div class="feature-label">LOCATIONS</div>
  </div>
  <div class="feature" style="left:529px">
    <div class="feature-circle"><svg width="50" height="50" viewBox="0 0 50 50" fill="none" stroke="#fff" stroke-width="2"><path d="M10 22l24-12 4 8-24 12z"/><path d="M38 18l4-2-3-7-4 2"/><path d="M22 27l-6 15M24 27l6 15M23 27v15"/></svg></div>
    <div class="feature-label">VISION</div>
  </div>
  <div class="feature" style="left:817px">
    <div class="feature-circle"><svg width="54" height="50" viewBox="0 0 54 50" fill="none" stroke="#fff" stroke-width="2"><path d="M4 18l8-6 8 3 6-3 8 2 8-4 8 6"/><path d="M12 12l-6 14 14 12 6 2 4-2 8-6 6-8"/><path d="M20 22l8 8M24 20l8 8M28 18l6 6"/></svg></div>
    <div class="feature-label">PARTNERS</div>
  </div>
</section>

<section class="strategy topic-dark">
  <h2 class="abs topic-title" style="left:62px;top:134px">IT Strategy Consulting</h2>
  <p class="abs topic-text" style="left:62px;top:190px">The success of any IT measure is decided long before the first line of the program. In addition to technical and specialist know-how, planning is primarily about intensive communication with future users. Early test planning helps ensure that requirements and functions match exactly.</p>
  <svg class="abs" style="left:580px;top:80px" width="560" height="320" viewBox="0 0 560 320">
    <g class="chart-label" text-anchor="end">
      <text x="48" y="15">$900,00</text><text x="48" y="38">$800,00</text><text x="48" y="61">$700,00</text><text x="48" y="84">$600,00</text><text x="48" y="107">$500,00</text><text x="48" y="130">$400,00</text><text x="48" y="153">$300,00</text><text x="48" y="176">$200,00</text><text x="48" y="199">$100,00</text><text x="48" y="222">$0</text>
    </g>
    <path d="M55 28l12-10v230l-12 10z" fill="#1d6b6e" opacity=".6"/>
    <path d="M55 258l12-10h330l-12 10z" fill="#dfe6ea"/>
    <g>
      <rect x="100" y="150" width="22" height="108" fill="var(--blue)"/><path d="M122 150l8-6v108l-8 6z" fill="#163e8f"/><path d="M100 150l8-6h22l-8 6z" fill="#4e7fe0"/>
      <rect x="126" y="180" width="22" height="78" fill="var(--teal)"/><path d="M148 180l8-6v78l-8 6z" fill="#1a7677"/><path d="M126 180l8-6h22l-8 6z" fill="#56c9c8"/>
      <rect x="152" y="240" width="22" height="18" fill="var(--orange)"/><path d="M174 240l8-6v18l-8 6z" fill="#9e3b18"/><path d="M152 240l8-6h22l-8 6z" fill="#f07a50"/>
      <rect x="212" y="90" width="22" height="168" fill="var(--blue)"/><path d="M234 90l8-6v168l-8 6z" fill="#163e8f"/><path d="M212 90l8-6h22l-8 6z" fill="#4e7fe0"/>
      <rect x="238" y="130" width="22" height="128" fill="var(--teal)"/><path d="M260 130l8-6v128l-8 6z" fill="#1a7677"/><path d="M238 130l8-6h22l-8 6z" fill="#56c9c8"/>
      <rect x="264" y="244" width="22" height="14" fill="var(--orange)"/><path d="M286 244l8-6v14l-8 6z" fill="#9e3b18"/><path d="M264 244l8-6h22l-8 6z" fill="#f07a50"/>
      <rect x="326" y="30" width="22" height="228" fill="var(--blue)"/><path d="M348 30l8-6v228l-8 6z" fill="#163e8f"/><path d="M326 30l8-6h22l-8 6z" fill="#4e7fe0"/>
      <rect x="352" y="105" width="22" height="153" fill="var(--teal)"/><path d="M374 105l8-6v153l-8 6z" fill="#1a7677"/><path d="M352 105l8-6h22l-8 6z" fill="#56c9c8"/>
      <rect x="378" y="244" width="22" height="14" fill="var(--orange)"/><path d="M400 244l8-6v14l-8 6z" fill="#9e3b18"/><path d="M378 244l8-6h22l-8 6z" fill="#f07a50"/>
    </g>
    <g class="chart-label" text-anchor="middle"><text x="135" y="284">Year 1</text><text x="247" y="284">Year 2</text><text x="362" y="284">Year 3</text></g>
    <g class="chart-label">
      <rect x="458" y="96" width="8" height="8" fill="var(--blue)"/><text x="480" y="104">Sales</text>
      <rect x="458" y="125" width="8" height="8" fill="var(--orange)"/><text x="480" y="133">Gross Margin</text>
      <rect x="458" y="154" width="8" height="8" fill="var(--teal)"/><text x="480" y="162">Net Profit</text>
    </g>
  </svg>
</section>

<section class="digital">
  <svg class="abs" style="left:40px;top:110px" width="560" height="290" viewBox="0 0 560 290">
    <g font-family="Open Sans, sans-serif" font-size="10.5" fill="#fff" text-anchor="end">
      <text x="143" y="30">Already Running</text><text x="143" y="44">Projects</text>
      <text x="143" y="86">Starting to investigate</text><text x="143" y="100">use cases or solutions</text>
      <text x="143" y="144">Planning to do so in the</text><text x="143" y="158">next 12 months</text>
      <text x="143" y="210">No Current plans</text>
    </g>
    <rect x="158" y="24" width="280" height="20" fill="var(--blue)"/><path d="M158 24l6-6h280l-6 6z" fill="#5a86e4"/><path d="M438 24l6-6v20l-6 6z" fill="#173f96"/>
    <rect x="158" y="82" width="176" height="20" fill="var(--orange)"/><path d="M158 82l6-6h176l-6 6z" fill="#f08060"/><path d="M334 82l6-6v20l-6 6z" fill="#9e3b18"/>
    <rect x="158" y="140" width="78" height="20" fill="#174b63"/><path d="M158 140l6-6h78l-6 6z" fill="#2f6f88"/><path d="M236 140l6-6v20l-6 6z" fill="#0e3042"/>
    <rect x="158" y="198" width="6" height="20" fill="var(--orange)"/>
    <g font-family="Exo 2, sans-serif" font-weight="700" font-size="30" fill="#fff">
      <text x="450" y="44">52%</text><text x="346" y="102">33%</text><text x="248" y="160">14%</text><text x="174" y="218">0%</text>
    </g>
    <g font-family="Open Sans, sans-serif" font-size="11" fill="#e6f4f4" text-anchor="middle">
      <text x="152" y="268">0</text><text x="204" y="268">10</text><text x="258" y="268">20</text><text x="313" y="268">30</text><text x="367" y="268">40</text><text x="421" y="268">50</text><text x="475" y="268">60</text>
    </g>
  </svg>
  <h2 class="abs topic-title" style="left:677px;top:126px">Digital Transformation</h2>
  <p class="abs topic-text" style="left:677px;top:186px;width:380px;color:#eef8f8">The digital upheaval is a reality and in full swing. In order to remain competitive, a profound change and rethinking in the company is necessary in the medium term. It's not about developing a new system or just improving processes. Rather, it is about profound changes in company processes on a procedural, technical and human level, supported by modern technologies.</p>
</section>

<section class="quality topic-dark">
  <div class="abs" style="left:0;top:0;width:1200px;height:449px" role="img" aria-label="City skyline at night with telecommunication towers"></div>
  <h2 class="abs topic-title" style="left:62px;top:142px">IT Quality Management</h2>
  <p class="abs topic-text" style="left:62px;top:198px">The success of any IT measure is decided long before the first line of the program. In addition to technical and specialist know-how, planning is primarily about intensive communication with future users. Early test planning helps ensure that requirements and functions match exactly.</p>
  <svg class="abs" style="left:600px;top:70px" width="560" height="360" viewBox="0 0 560 360">
    <g transform="translate(210,175)">
      <path d="M-190 0v40a190 92 0 0 0 380 0v-40z" fill="#a73d17"/>
      <path d="M0 0L-190 0A190 92 0 0 0 190 0z" fill="var(--orange)"/>
      <path d="M0 0L190 0A190 92 0 0 0 163-47z" fill="#0d3d55"/>
      <path d="M190 0v40l-27-47z" fill="#082a3c"/>
      <path d="M-4-6L-150-58A190 92 0 0 1 -33-96z" fill="var(--orange)"/>
      <path d="M-14-12L-178-28A190 92 0 0 1 -10-94z" fill="var(--blue)"/>
      <path d="M-10 -40v28" stroke="none"/>
      <path d="M4-14L60-92A190 92 0 0 1 110-80z" fill="var(--teal)"/>
      <path d="M6-12L112-78A190 92 0 0 1 150-60z" fill="#5b4a78"/>
      <path d="M8-8L156-54A190 92 0 0 1 178-30z" fill="#114a63"/>
    </g>
    <g font-family="Open Sans, sans-serif" font-size="11" fill="#fff">
      <text x="76" y="10">Automotive and</text><text x="76" y="24">Telecommunications (24.6%)</text>
      <text x="306" y="40">Transport And</text><text x="306" y="54">Storage (6.9%)</text>
      <text x="386" y="94">Business</text><text x="386" y="108">Services (6.9%)</text>
      <text x="400" y="180">Other</text><text x="400" y="194">Services (12.0%)</text>
      <text x="76" y="346">Number of Establishments ($31,137)</text>
    </g>
  </svg>
</section>

<section class="portfolio">
  <h2 class="section-title"><b>Portfolio</b></h2>
  <div class="sub">Aur The Essential Focus</div>
  <p class="intro">Our range of services covers the management of the entire development process from applications and extensions to quality assurance through to going live and support afterwards.</p>
  <div class="card" style="left:167px;top:247px">
    <div class="card-media" role="img" aria-label="Technician working on a telecommunication tower" style="background:linear-gradient(160deg,#aebfcc,#5d6d7a 60%,#2d3640)"></div>
    <div class="card-title" style="margin-top:18px">Projects In Excellence</div>
    <div class="card-desc">We manage projects according to the PMQA Competence</div>
  </div>
  <div class="card" style="left:613px;top:247px">
    <div class="card-media" role="img" aria-label="Cloud network graphic on teal background" style="background:radial-gradient(circle at 50% 50%,#6fd0cf,#2aa5a5 60%,#1f8f90)"></div>
    <div class="card-title">Cloud Transition</div>
    <div class="card-desc">Wir managen Projekte nach der PMQA Competence Basel</div>
  </div>
  <div class="card" style="left:167px;top:607px">
    <div class="card-media" role="img" aria-label="Engineer with laptop next to an industrial robot arm" style="background:linear-gradient(100deg,#c8d0d6,#8c98a2 45%,#c9b84a 80%,#6b6f55)"></div>
    <div class="card-title" style="margin-top:30px">Digitalization</div>
    <div class="card-desc">Wir managen Projekte nach der PMQA Competence Basel</div>
  </div>
  <div class="card" style="left:613px;top:607px">
    <div class="card-media" role="img" aria-label="Business meeting in a modern conference room" style="background:linear-gradient(150deg,#3a5468,#1d2d3b 55%,#4d6476)"></div>
    <div class="card-title">Consulting In Excellence</div>
    <div class="card-desc">Wir managen Projekte nach der PMQA Competence Basel</div>
  </div>
</section>

<section class="contact">
  <div class="contact-bg"></div>
  <h2 class="section-title"><b>Please</b> Contact Us !</h2>
  <div class="sub">Need an have Any Question for Contact us Today !</div>
  <div class="field" style="left:262px;top:183px;width:331px">First Name *</div>
  <div class="field" style="left:607px;top:183px;width:331px">Last Name *</div>
  <div class="field" style="left:262px;top:237px;width:331px">Refrence *</div>
  <div class="field" style="left:607px;top:237px;width:331px">Email *</div>
  <div class="field" style="left:262px;top:292px;width:676px;height:74px">Message *</div>
  <div class="submit">SUBMIT</div>
</section>

<section class="experience">
  <div class="exp-media" role="img" aria-label="Hand holding a tablet showing a bar chart of worldwide IT spending" style="background:linear-gradient(120deg,#dfe3e6,#b9c2c9 40%,#2d3b4a 62%,#5b87b8 85%,#e9ebec)"></div>
  <div class="abs exp-lead">If More than</div>
  <div class="abs exp-title">25 Years Of Experience</div>
  <p class="abs exp-text">Is Just Good Enough for you, We Look Forward to Hearing from you!</p>
  <div class="abs exp-phone">
    <div class="ring"><div class="icon-circle"><svg width="28" height="28" viewBox="0 0 24 24"><path fill="#fff" d="M6.6 10.8a15.1 15.1 0 0 0 6.6 6.6l2.2-2.2c.3-.3.7-.4 1-.2 1.1.4 2.3.6 3.6.6.6 0 1 .4 1 1V20c0 .6-.4 1-1 1A17 17 0 0 1 3 4c0-.6.4-1 1-1h3.5c.6 0 1 .4 1 1 0 1.3.2 2.5.6 3.6.1.3 0 .7-.2 1z"/></svg></div></div>
    <div><small>Call Us On:</small><strong>+49 (0) 5521 7704410</strong></div>
  </div>
</section>

<footer class="footer">
  <div class="abs brand">
    <div class="brand-name"><span class="brand-dot"></span>Tervork Consulting</div>
    <div class="brand-tag">power of competence</div>
  </div>
  <p class="abs footer-text">Whether IT project management, consulting, commissioning management or system integration: With Tervork Consulting you create the best conditions for IT systems that do what they should. In compliance with all time and cost specifications. <a href="#">Read More</a></p>
  <div class="abs sitemap">
    <div class="footer-heading">SITEMAP</div>
    <ul><li>Home</li><li>Companies</li><li>Portfolio</li><li>Scouting</li><li>Contact Us</li></ul>
  </div>
  <div class="abs contact-info">
    <div class="footer-heading">CONTACT US</div>
    <div class="info-row" style="top:40px">
      <div class="info-icon"><svg width="14" height="18" viewBox="0 0 14 18"><path fill="#fff" d="M7 0a7 7 0 0 0-7 7c0 5 7 11 7 11s7-6 7-11a7 7 0 0 0-7-7zm0 9.5A2.5 2.5 0 1 1 7 4.5a2.5 2.5 0 0 1 0 5z"/></svg></div>
      <div>Tervork Consulting GmbH<br>Werkstraße 14 – 16 D-37412<br>Auendorf</div>
    </div>
    <div class="info-row" style="top:112px">
      <div class="info-icon"><svg width="16" height="16" viewBox="0 0 24 24"><path fill="#fff" d="M6.6 10.8a15.1 15.1 0 0 0 6.6 6.6l2.2-2.2c.3-.3.7-.4 1-.2 1.1.4 2.3.6 3.6.6.6 0 1 .4 1 1V20c0 .6-.4 1-1 1A17 17 0 0 1 3 4c0-.6.4-1 1-1h3.5c.6 0 1 .4 1 1 0 1.3.2 2.5.6 3.6.1.3 0 .7-.2 1z"/></svg></div>
      <div>+49 (0) 5521 7704410<br>+49 (0) 5521 7704411</div>
    </div>
    <div class="info-row" style="top:170px">
      <div class="info-icon"><svg width="16" height="12" viewBox="0 0 16 12"><path fill="#fff" d="M0 0h16v12H0zM1.5 1.5L8 6.5l6.5-5"/><path d="M1 1l7 5.5L15 1" stroke="#2aa9a9" fill="none" stroke-width="1.5"/></svg></div>
      <div style="line-height:30px">info@t-vork.com</div>
    </div>
  </div>
  <div class="abs copyright">©2021 <span>Tervork Consulting GmbH</span> - All right reserved.</div>
</footer>

</body>
</html>
```